VELMIRAN (coffee package design)

Make coffee bag for coffee beans: VELMIRAN is a quality-driven coffee roaster focused on crafting fresh, flavorful coffee from premium beans sourced directly from farms. We build close relationships with growers to ensure ethical practices, traceability, and exceptional quality at the origin. Our small-batch roasting approach brings out the unique character of each bean—highlighting bold notes, rich complexity, and peak freshness. At VELMIRAN, we believe great coffee starts at the source—and ends in your cup, roasted to perfection.

**VELMIRAN** is a quality-driven coffee roaster focused on crafting fresh, flavorful coffee from **premium beans sourced directly from farms**. We build close relationships with growers to ensure ethical practices, traceability, and exceptional quality at the origin. Our small-batch roasting approach brings out the unique character of each bean—highlighting bold notes, rich complexity, and peak freshness. At **VELMIRAN**, we believe great coffee starts at the source—and ends in your cup, roasted to perfection.

VELMIRAN

ETHICALLY SOURCED COFFEE

On Top: 100% Arabica Beans

On Left Side:
Coffee brew guide: https://in.brewboardly.com/pin/318274659201847362/
https://in.brewboardly.com/pin/coffee-brewing-method-chart--207431985562143/

On right side bottom:
STORAGE
Proper storage is essential to maintaining your coffee’s freshness and flavor. Once opened, we recommend keeping your coffee in a cool, dark, dry place and sealed in an airtight container. Always reseal the bag after each use to preserve maximum freshness and aroma.

487 Tullane Street Oakland Ca 94619

Follow Us
www.velmiran.com
TikTok@velmiran
IG@getvelmiran

Target Market(s)

Coffee/ Cafe

Industry/Entity Type

Coffee

Font styles to use
Other font styles liked:
• Non‑Seasonal Sans

Requirements
Must have
• Clean, modern
Nice to have
• Elegant

```html
<!DOCTYPE html>
<html lang="en">
<head>
<meta charset="utf-8">
<title>VELMIRAN – Coffee Bag Dieline</title>
<link href="https://fonts.googleapis.com/css2?family=Gloock&family=Archivo:wght@400;500;600;700;800&display=swap" rel="stylesheet">
<style>
  :root{
    --stage:#e4e4e2;
    --teal-side:#17606a;
    --teal-front:#154a54;
    --label-green:#9caa64;
    --cream:#f4efc8;
    --ink:#1f3b33;
    --orange:#d0532a;
    --rust:#8f2d1f;
    --leaf:#236b3a;
    --line:#7d8a4e;
  }
  *{box-sizing:border-box;margin:0;padding:0}
  html,body{width:811px;height:1200px;overflow:hidden;background:var(--stage)}
  body{font-family:"Archivo",Arial,sans-serif;position:relative}

  .dieline{position:absolute;left:0;top:270px;width:811px;height:660px;overflow:hidden}
  .side-panel{position:absolute;top:0;height:100%;width:203px;background:var(--teal-side)}
  .side-panel--left{left:0}
  .side-panel--right{left:608px}
  .front-panel{position:absolute;left:203px;top:0;width:405px;height:100%;background:var(--teal-front)}

  /* pinked edges */
  .pinked{position:absolute;background:var(--label-green)}
  .pinked::before,.pinked::after{content:"";position:absolute;left:0;right:0;height:4px;
    background-size:6px 6px;background-repeat:repeat-x}
  .pinked::before{top:-4px;
    background-image:linear-gradient(45deg,var(--label-green) 50%,transparent 50%),
                     linear-gradient(-45deg,var(--label-green) 50%,transparent 50%);
    background-position:0 100%}
  .pinked::after{bottom:-4px;
    background-image:linear-gradient(135deg,var(--label-green) 50%,transparent 50%),
                     linear-gradient(225deg,var(--label-green) 50%,transparent 50%)}
  .pinked--bottom-only::before{display:none}

  /* origin label */
  .origin-label{left:65px;top:0;width:275px;height:397px;color:var(--ink)}
  .origin-art{position:absolute;left:0;top:0;width:275px;height:239px;
    background:
      radial-gradient(ellipse at 62% 35%,#3d7a3c 0 28%,transparent 29%),
      radial-gradient(ellipse at 35% 75%,var(--orange) 0 30%,transparent 31%),
      linear-gradient(160deg,var(--label-green) 0 40%,#b6683a 70%,var(--label-green))}
  .origin-name{position:absolute;top:250px;left:0;width:100%;text-align:center;
    font-weight:700;font-size:26px;color:var(--orange);letter-spacing:.5px}
  .origin-rule{position:absolute;left:0;width:100%;height:1px;background:var(--line)}
  .origin-desc{position:absolute;top:283px;left:0;width:100%;text-align:center;font-size:6.8px;line-height:10px;color:#2a3a26}
  .spec-row{position:absolute;top:310px;left:0;width:100%;height:28px;display:flex}
  .spec-cell{font-size:5.4px;letter-spacing:.2px;display:flex;align-items:center;justify-content:center;border-right:1px solid var(--line);color:#2a3a26}
  .spec-cell:last-child{border-right:none}
  .roast-title{position:absolute;top:345px;width:100%;text-align:center;font-size:5.8px;font-weight:600}
  .roast-scale{position:absolute;top:360px;left:45px;display:flex;gap:2px}
  .roast-dot{width:17px;height:17px;border-radius:50%;border:1px solid var(--leaf)}
  .roast-dot--active{background:var(--orange);border-color:var(--orange)}
  .roast-meta{position:absolute;top:385px;left:45px;width:190px;display:flex;justify-content:space-between;font-size:6.4px;font-weight:500}

  /* brand block */
  .brand-name{position:absolute;left:0;width:100%;top:466px;text-align:center;font-family:"Gloock",Georgia,serif;
    font-size:86px;line-height:1;color:var(--cream);transform:scaleX(.86);letter-spacing:-1px}
  .brand-tagline{position:absolute;left:0;width:100%;top:559px;text-align:center;font-weight:700;font-size:11.5px;letter-spacing:.6px;color:var(--cream)}
  .brand-beans{position:absolute;left:0;width:100%;top:635px;text-align:center;font-weight:700;font-size:8.5px;letter-spacing:.4px;color:var(--cream)}

  /* brew guide */
  .brew-guide{left:41px;top:180px;width:120px;height:446px}
  .brew-card{position:absolute;left:17px;width:81px;height:56px;border:1px solid var(--cream);border-radius:7px;color:var(--cream)}
  .brew-title{position:absolute;left:5px;top:3px;font-size:5.6px;font-weight:800;letter-spacing:.2px;font-variant:small-caps}
  .brew-facts{position:absolute;left:5px;top:12px;list-style:none;font-size:3.4px;line-height:10px;letter-spacing:.2px}
  .brew-facts li::before{content:"";display:inline-block;width:5px;height:5px;border:.7px solid var(--cream);border-radius:1px;margin-right:3px;vertical-align:-1px}
  .brew-tool{position:absolute;right:-5px;bottom:2px;width:22px;height:26px;border-radius:3px;background:rgba(244,239,200,.35)}

  /* storage */
  .storage{left:15px;top:256px;width:174px;height:293px}
  .storage-inner{position:absolute;left:0;top:293px;width:293px;height:174px;transform-origin:0 0;transform:rotate(-90deg);color:var(--cream)}
  .storage-title{position:absolute;left:76px;top:12px;font-weight:800;font-size:31px;letter-spacing:1px;line-height:1}
  .storage-copy{position:absolute;left:14px;top:52px;width:265px;font-size:6.9px;line-height:10.2px;text-align:center}
  .storage-divider{position:absolute;left:0;width:100%;height:1px;background:rgba(244,239,200,.35)}
  .follow-row{position:absolute;left:14px;top:107px;width:265px;height:31px;display:flex;font-size:5.4px;letter-spacing:.2px}
  .follow-row span{flex:1;display:flex;align-items:center;justify-content:center;border-right:1px solid rgba(244,239,200,.35)}
  .follow-row span:last-child{border-right:none}
  .storage-address{position:absolute;left:0;width:100%;text-align:center;top:151px;font-size:7px;letter-spacing:.3px}
</style>
</head>
<body>
<main class="dieline">
  <section class="side-panel side-panel--left" role="img" aria-label="Teal side gusset with geometric chevron pattern">
    <div class="pinked brew-guide">
      <article class="brew-card" style="top:15px">
        <h3 class="brew-title">Drip Coffee</h3>
        <ul class="brew-facts"><li>2 TBSP · 6 OZ</li><li>MEDIUM COARSE</li><li>3-4 MIN</li><li>95-165 MG CAFFEINE</li></ul>
        <div class="brew-tool" role="img" aria-label="Drip coffee pot icon"></div>
      </article>
      <article class="brew-card" style="top:86px">
        <h3 class="brew-title">Carafe Pour</h3>
        <ul class="brew-facts"><li>5 TBSP · 16 OZ</li><li>MEDIUM COARSE</li><li>4-5 MIN</li><li>125 MG CAFFEINE</li></ul>
        <div class="brew-tool" role="img" aria-label="Glass carafe brewer icon"></div>
      </article>
      <article class="brew-card" style="top:157px">
        <h3 class="brew-title">Espresso Machine</h3>
        <ul class="brew-facts"><li>7 G · 1.4 OZ</li><li>FINE</li><li>1 MIN</li><li>47-75 MG CAFFEINE</li></ul>
        <div class="brew-tool" role="img" aria-label="Espresso machine icon"></div>
      </article>
      <article class="brew-card" style="top:228px">
        <h3 class="brew-title">Pour Over</h3>
        <ul class="brew-facts"><li>3 TBSP · 8 OZ</li><li>MEDIUM</li><li>3-4 MIN</li><li>175 MG CAFFEINE</li></ul>
        <div class="brew-tool" role="img" aria-label="Pour over dripper icon"></div>
      </article>
      <article class="brew-card" style="top:300px">
        <h3 class="brew-title">French Press</h3>
        <ul class="brew-facts"><li>6 TBSP · 18 OZ</li><li>COARSE</li><li>4 MIN</li><li>80-107 MG CAFFEINE</li></ul>
        <div class="brew-tool" role="img" aria-label="French press icon"></div>
      </article>
      <article class="brew-card" style="top:371px">
        <h3 class="brew-title">Cold Brew</h3>
        <ul class="brew-facts"><li>10 TBSP · 16 OZ</li><li>EXTRA COARSE</li><li>12-48 HR</li><li>153-238 MG CAFFEINE</li></ul>
        <div class="brew-tool" role="img" aria-label="Iced coffee glass icon"></div>
      </article>
    </div>
  </section>

  <section class="front-panel">
    <div class="pinked pinked--bottom-only origin-label">
      <div class="origin-art" role="img" aria-label="Illustration of a coffee plant with red cherries beside an orange cup being filled with coffee"></div>
      <h2 class="origin-name">SIDAMO</h2>
      <div class="origin-rule" style="top:280px"></div>
      <p class="origin-desc">Grown in the Sidamo region south of Addis Ababa, Ethiopia's capitol city.<br>The region is well known for having the ideal climate for growing coffee.</p>
      <div class="origin-rule" style="top:310px"></div>
      <div class="spec-row">
        <div class="spec-cell" style="width:75px">ORIGIN: ETHIOPIA</div>
        <div class="spec-cell" style="width:64px">VAR.: CASTILLO</div>
        <div class="spec-cell" style="width:75px">PROC: FULLY WASHED</div>
        <div class="spec-cell" style="width:61px">ALT.: 1,800 MASL</div>
      </div>
      <div class="origin-rule" style="top:338px"></div>
      <p class="roast-title">ROAST LEVEL</p>
      <div class="roast-scale">
        <span class="roast-dot"></span><span class="roast-dot"></span><span class="roast-dot roast-dot--active"></span><span class="roast-dot"></span><span class="roast-dot"></span><span class="roast-dot"></span><span class="roast-dot"></span><span class="roast-dot"></span><span class="roast-dot"></span><span class="roast-dot"></span>
      </div>
      <div class="roast-meta"><span>WHOLE BEAN</span><span>ROASTED ON: 02 20 2020</span></div>
    </div>
    <h1 class="brand-name">VELMIRAN</h1>
    <p class="brand-tagline">ETHICALLY SOURCED COFFEE</p>
    <p class="brand-beans">100% ARABICA BEANS</p>
  </section>

  <section class="side-panel side-panel--right" role="img" aria-label="Teal side gusset with geometric chevron pattern">
    <div class="pinked storage">
      <div class="storage-inner">
        <h2 class="storage-title">STORAGE</h2>
        <p class="storage-copy">Proper storage is essential to maintaining your coffee's freshness and flavor. Once opened, we recommend keeping your coffee in a cool, dark, dry place and sealed in an airtight container. Always reseal the bag after each use to preserve maximum freshness and aroma.</p>
        <div class="storage-divider" style="top:107px"></div>
        <div class="follow-row"><span>FOLLOW US</span><span>VELMIRAN.COM</span><span>@VELMIRAN</span><span>@GETVELMIRAN</span></div>
        <div class="storage-divider" style="top:138px"></div>
        <p class="storage-address">487 TULLANE STREET OAKLAND CA 94619</p>
      </div>
    </div>
  </section>
</main>
</body>
</html>
```